Mental Health Therapy Website

I need a design for a mental health therapy website. It is a private practice. The business name is Hale Wellspring, PLLC. My name is Martin Hale, LMHC, NCC, DCC. I would like some of the features/menus to be Home; Welcome/About Me, Rates and Services, Common Questions, and Contact.
If possible I would like a blog on the main page that I can update with articles I write. I would like the contact page to feature a map to my location (4316 Fernbrook Ave. S, Lakewood, WA 98421).
I would like to place a small photo of me on the Welcome/About page.
I am new to this so if I am forgetting anything, please ask me!!
I will upload my logo so you can fit it and the color scheme into the design.
Thank you so very much!

```html
<!DOCTYPE html>
<html lang="en">
<head>
<meta charset="utf-8">
<title>Hale Wellspring, PLLC</title>
<link rel="stylesheet" href="https://fonts.googleapis.com/css2?family=Noto+Sans:wght@400;700&family=Noto+Serif:wght@400;700&display=swap">
<style>
  :root {
    --blue: #2f5f97;
    --green: #78a53b;
    --text: #666666;
    --muted: #999999;
    --panel: #f0f0f0;
    --white: #ffffff;
    --frame: #a8a8a8;
  }
  * { box-sizing: border-box; margin: 0; padding: 0; }
  html, body { width: 1200px; height: 861px; overflow: hidden; background: var(--white); }
  body { font-family: "Noto Sans", sans-serif; color: var(--text); }
  .page { width: 982px; margin-left: 109px; position: relative; }

  .site-header { height: 109px; position: relative; }
  .brand { position: absolute; left: 0; top: 30px; display: flex; align-items: center; gap: 12px; }
  .brand-mark { width: 46px; height: 46px; border-radius: 50%; background: var(--green); }
  .brand-name { font-family: "Noto Serif", serif; font-weight: 700; font-size: 28px; color: var(--blue); line-height: 1; }
  .contact-block { position: absolute; right: 0; top: 14px; text-align: right; font-family: "Noto Serif", serif; }
  .phone { font-family: "Noto Sans", sans-serif; font-weight: 700; font-size: 28px; color: var(--blue); line-height: 1.1; }
  .address { font-size: 13px; line-height: 15px; color: var(--text); }

  .main-nav { height: 55px; background: var(--green); display: flex; align-items: center; padding-left: 34px; gap: 0; }
  .main-nav a { font-family: "Noto Serif", serif; font-weight: 700; font-size: 16px; color: var(--white); text-decoration: none; text-shadow: 1px 1px 2px rgba(0,0,0,.45); margin-right: 34px; }

  .content { display: flex; justify-content: space-between; margin-top: 18px; }
  .blog { width: 595px; }
  .post { margin-bottom: 16px; }
  .post-title { font-family: "Noto Serif", serif; font-weight: 700; font-size: 26px; color: var(--blue); line-height: 1.2; }
  .post-date { font-size: 15px; color: var(--muted); margin: 8px 0 3px; }
  .post p { font-size: 15px; line-height: 23px; margin-bottom: 23px; }
  .post p:last-of-type { margin-bottom: 9px; }
  .comments { font-weight: 700; font-size: 15px; color: var(--green); text-decoration: none; }

  .sidebar { width: 338px; }
  .about-card { background: var(--panel); padding: 16px 8px 24px 14px; }
  .about-card h3 { font-family: "Noto Serif", serif; font-weight: 700; font-size: 15px; color: var(--green); margin-bottom: 10px; }
  .portrait { display: block; width: 292px; height: 229px; margin-left: 10px; border: 1px solid var(--frame); background: linear-gradient(135deg, #e9edf3 0%, #cdd5e2 55%, #dfc6c0 100%); }
  .about-card p { font-size: 12px; line-height: 20px; margin-top: 9px; }

  .sidebar-heading { font-family: "Noto Serif", serif; font-weight: 700; font-size: 22px; color: var(--green); margin: 20px 0 4px; }
  .latest-posts { list-style: none; }
  .latest-posts a { font-family: "Noto Serif", serif; font-size: 18px; line-height: 31px; color: var(--blue); text-decoration: none; }
  .social { display: flex; gap: 10px; margin-top: 8px; }
  .social a { width: 35px; height: 35px; border-radius: 4px; background: var(--blue); display: block; }
</style>
</head>
<body>
<div class="page">
  <header class="site-header">
    <div class="brand">
      <span class="brand-mark"></span>
      <span class="brand-name">Hale Wellspring</span>
    </div>
    <div class="contact-block">
      <div class="phone">024 76 555 018</div>
      <div class="address">4316 Fernbrook Ave. S<br>Lakewood<br>WA 98421</div>
    </div>
  </header>

  <nav class="main-nav">
    <a href="#">Home</a>
    <a href="#">About Me</a>
    <a href="#">Rates and Services</a>
    <a href="#">Common Questions</a>
    <a href="#">Contact</a>
  </nav>

  <div class="content">
    <main class="blog">
      <article class="post">
        <h2 class="post-title">This is a blog post title</h2>
        <div class="post-date">22nd January 2014</div>
        <p>Lorem ipsum dolor sit amet, eius debitis scribentur ne vix, eu error deseruisse sed, dicat interesset in eam. Sea vide aliquando id. Vocent audire viderer mei at, sea at mucius labore dignissim. Mea virtute liberavisse et, at usu adhuc dolores qualisque. In qui tollit epicurei sadipscing, timeam prompta eligendi qui ea, ea duo harum pertinax. Cibo laboramus vix at.</p>
        <p>Ei vitae sanctus necessitatibus per. Omnis essent vivendum mel ne, ad nemore doctus integre usu. Per cu audire definitionem, ei facer vituperatoribus cum, eam in graeco maluisset. Has explicari urbanitas democritum no, sed sale mazim praesent eu, mundi alterum te sed.</p>
        <p>Est no diam agam sadipscing. Eum solet moderatius te, pri blandit ullamcorper ea. Dicat tempor debitis ne duo, ei nam recusabo argumentum. Ad qui laudem viderer discere. Semper facete accusata sit eu</p>
        <a class="comments" href="#">3 comments</a>
      </article>
      <article class="post">
        <h2 class="post-title">And another blog post title</h2>
        <div class="post-date">22nd January 2014</div>
        <p>Lorem ipsum dolor sit amet, eius debitis scribentur ne vix, eu error deseruisse sed, dicat interesset in eam. Sea vide aliquando id. Vocent audire viderer mei at, sea at mucius labore dignissim. Mea virtute liberavisse et, at usu adhuc dolores qualisque. In qui tollit epicurei sadipscing, timeam prompta eligendi qui ea, ea duo harum pertinax. Cibo laboramus vix at.</p>
        <p>Ei vitae sanctus necessitatibus per. Omnis essent vivendum mel ne, ad nemore doctus integre usu. Per cu audire definitionem, ei facer vituperatoribus cum, eam in graeco maluisset.</p>
      </article>
    </main>

    <aside class="sidebar">
      <section class="about-card">
        <h3>My name is Martin Hale, LMHC, NCC, DCC.</h3>
        <div class="portrait" role="img" aria-label="Portrait photo of Martin Hale"></div>
        <p>Est no diam agam sadipscing. Eum solet moderatius te, pri blandit ullamcorper ea. Dicat tempor debitis ne duo, ei nam recusabo argumentum. Ad qui laudem viderer discere. Semper facete accusata sit eu</p>
      </section>

      <h3 class="sidebar-heading">Latest Posts</h3>
      <ul class="latest-posts">
        <li><a href="#">This is a blog post title</a></li>
        <li><a href="#">And another blog post title</a></li>
        <li><a href="#">Benefits on meditation</a></li>
        <li><a href="#">Symptoms of Depression</a></li>
        <li><a href="#">Yet another blog post depresssion</a></li>
      </ul>

      <h3 class="sidebar-heading">Follow me on Social Media</h3>
      <div class="social">
        <a href="#" aria-label="Social profile one"></a>
        <a href="#" aria-label="Social profile two"></a>
        <a href="#" aria-label="Social profile three"></a>
        <a href="#" aria-label="Social profile four"></a>
      </div>
    </aside>
  </div>
</div>
</body>
</html>
```